Create a Brochure Design for Brantley Homecare

Brantley Homecare is a subsidiary of the Brantley Care Group. This brochure is specifically for the Brantley Homecare company and brand. Create a 3 panel, A4, front and back, tri-fold brochure. This brochure will be a way to introduce our Homecare services to the community, prospective clients, and various referral partners. The brochure must be eye catching, unique in its deliverables and demonstrate both attention to detail and comfort. Our organization is sophisticated and built around warmth, care and individualized personal attention. The most important aspect of this design is to focus on creating a nurturing, warm, and inviting feel where you would want to have a Nurse or Nurse’s Aide in your own home or a loved one’s home.

I am open to the creativity of the designer to develop something based on the above criteria; however I would like the design to work well with the existing collateral material. What I mean by that is that while I want everything to have its own personality and stand out as its own brand representative, I still need to be able to tell that the overall design concept stays stylistically inside of the same ‘family’ of existing designed material. Because of this, below I would like for the designer to pull inspiration from the link to our website (Located below) as well as from the attachment of our recently refreshed business cards (Attached). This should allow each design to be unique and creative, while still staying inside of a framework and the feel/style that I am looking for.

Finally, I want all the designers to understand that this brochure design is for a private, in home, healthcare company where we are responsible for providing personalized care for a culturally and ethnically diverse make-up clientele of all ages. The photos that are used must represent an image of warmth, care, and a positive interaction between client and caregiver.

Look under the Brantley Homecare tab at www.brantleycaregroup-example.net

Industry/Entity Type

Healthcare

Requirements
Must have
• • The Brantley Homecare company logo must be included.

```html
<!DOCTYPE html>
<html lang="en">
<head>
<meta charset="utf-8">
<title>Brantley Homecare – Tri-fold Brochure</title>
<link href="https://fonts.googleapis.com/css2?family=Crimson+Pro:wght@400;600&display=swap" rel="stylesheet">
<style>
  :root{
    --backdrop:#4b4f54;
    --cream:#fbf1dc;
    --salmon:#f1957c;
    --green:#1f6e5c;
    --ink:#4a3f35;
    --white:#ffffff;
  }
  *{box-sizing:border-box;margin:0;padding:0}
  html,body{width:1200px;height:800px;overflow:hidden}
  body{
    background:var(--backdrop);
    font-family:"Crimson Pro",Georgia,serif;
    color:var(--ink);
    position:relative;
  }
  .brochure{
    position:absolute;left:60px;top:18px;
    width:1080px;height:764px;
    display:flex;
  }
  .panel{position:relative;width:360px;height:100%;background:var(--cream);overflow:hidden}
  .panel + .panel{border-left:1px solid rgba(0,0,0,.06)}
  .photo{position:absolute;left:0;width:100%}
  .band{position:absolute;left:0;width:100%;display:block}

  /* Panel 1 – service feature */
  .service .photo{top:0;height:560px;
    background:linear-gradient(160deg,#d9c3a0 0%,#b59c86 40%,#6f7496 70%,#c8b49a 100%)}
  .service .band{top:390px;height:374px}
  .service-copy{position:absolute;left:36px;right:34px;top:470px;color:var(--white)}
  .service-title{font-size:30px;font-weight:400;margin-bottom:14px}
  .service-copy p{font-size:15px;line-height:1.4;margin-bottom:12px}

  /* Brand lockup */
  .brand{display:flex;align-items:center;gap:12px;color:var(--green);font-weight:600}
  .brand-mark{width:34px;height:34px;background:var(--salmon);flex:none}
  .brand-name{font-size:30px;line-height:1}

  /* Panel 2 – contact */
  .contact .brand{position:absolute;left:50px;top:300px}
  .contact-info{position:absolute;left:62px;top:400px;font-size:17px;line-height:1.35;color:var(--ink)}
  .contact-title{font-size:18px;margin-bottom:10px;font-weight:400}
  .contact-info address{font-style:normal}

  /* Panel 3 – cover */
  .cover .brand{position:absolute;left:50px;top:90px}
  .cover .photo{top:180px;height:584px;
    background:linear-gradient(180deg,#b9d3e6 0%,#dfe6e8 30%,#a79a86 60%,#8c7a66 100%)}
  .cover .band-top{top:178px;height:60px}
  .cover .band-bottom{top:530px;height:234px}
  .tagline{position:absolute;left:32px;right:20px;top:612px;color:var(--white);
    font-size:27px;line-height:1.2;font-weight:400}
</style>
</head>
<body>
  <main class="brochure">

    <section class="panel service">
      <div class="photo" role="img" aria-label="Photo of a caregiver helping an older woman sort her weekly medication at a kitchen counter"></div>
      <svg class="band" viewBox="0 0 360 374" preserveAspectRatio="none" aria-hidden="true">
        <path d="M0 30 C120 40 250 70 360 120 L360 374 L0 374 Z" fill="var(--salmon)"/>
      </svg>
      <div class="service-copy">
        <h2 class="service-title">Medication Services</h2>
        <p>Brantley Homecare clients who already receive personal care services may choose to have a licensed nurse pre-pour their medication into weekly pill containers for a one to four week period.</p>
        <p>A list of medications, including over-the-counter items, will be provided to the physician for written authorization.</p>
      </div>
    </section>

    <section class="panel contact">
      <div class="brand">
        <span class="brand-mark"></span>
        <span class="brand-name">Brantley Homecare</span>
      </div>
      <div class="contact-info">
        <h3 class="contact-title">Contact Us:</h3>
        <address>
          Brantley Homecare<br>
          480 Maple Grove Ave.<br>
          Suite #210<br>
          Tel.: 555-010-7319<br>
          Fax: 555-010-7320<br>
          info@brantleycare-example.com
        </address>
      </div>
    </section>

    <section class="panel cover">
      <div class="brand">
        <span class="brand-mark"></span>
        <span class="brand-name">Brantley Homecare</span>
      </div>
      <div class="photo" role="img" aria-label="Photo of a caregiver with an older man in a wheelchair enjoying the seaside on a sunny boardwalk"></div>
      <svg class="band band-top" viewBox="0 0 360 60" preserveAspectRatio="none" aria-hidden="true">
        <path d="M0 0 L360 0 L360 40 C240 10 120 10 0 30 Z" fill="var(--cream)"/>
      </svg>
      <svg class="band band-bottom" viewBox="0 0 360 234" preserveAspectRatio="none" aria-hidden="true">
        <path d="M0 20 C120 50 240 60 360 40 L360 234 L0 234 Z" fill="var(--salmon)"/>
      </svg>
      <p class="tagline">Someone you can depend on.<br>Without question.</p>
    </section>

  </main>
</body>
</html>
```